Business card and stationary for tattoo photography company
Velvet Harbor Photography
Business card and stationary for tattoo photography company - Photography
Creative Brief
Modern
Rolf Lindqvist
Photographer / Owner
4630 Marlow Ave W Parrish, FL 34218
rolf@velvetharborphotoworks.com
www.velvetharborphotoworks.com
Strength, Elegance, and Beauty

```html
<!DOCTYPE html>
<html lang="en">
<head>
<meta charset="utf-8">
<title>Velvet Harbor Photography — Stationery</title>
<link rel="stylesheet" href="https://fonts.googleapis.com/css2?family=Raleway:wght@400;600&family=Mrs+Saint+Delafield&display=swap">
<style>
  :root {
    --bg: #e6e6e6;
    --paper: #ffffff;
    --ink: #3a3a3a;
    --ink-soft: #8a8a8a;
    --accent: #b5344a;
    --notebook: #151515;
    --binding: #9a9a9a;
    --shadow: 0 6px 18px rgba(0,0,0,0.12);
  }
  * { box-sizing: border-box; margin: 0; padding: 0; }
  html, body { width: 1200px; height: 674px; overflow: hidden; }
  body {
    background: var(--bg);
    font-family: "Raleway", sans-serif;
    color: var(--ink);
    position: relative;
  }
  .sheet { position: absolute; background: var(--paper); box-shadow: var(--shadow); overflow: hidden; }

  .brand { display: flex; align-items: center; gap: 6px; font-weight: 600; color: var(--ink); white-space: nowrap; }
  .brand-dot { border-radius: 50%; background: var(--accent); flex: none; }

  /* Business card front */
  .card-front { left: 60px; top: 70px; width: 220px; height: 126px; padding: 16px; }
  .card-front .brand { font-size: 13px; }
  .card-front .brand-dot { width: 7px; height: 7px; }
  .card-front .person { margin-top: 18px; font-size: 9px; font-weight: 600; }
  .card-front .role { font-size: 7px; color: var(--ink-soft); margin-bottom: 6px; }
  .card-front .contact { font-size: 6.5px; line-height: 1.45; }

  /* Business card back */
  .card-back { left: 60px; top: 212px; width: 220px; height: 126px; }
  .card-back .photo { width: 100%; height: 100%; background: linear-gradient(120deg, #1c1c1c 0%, #5a5a5a 45%, #cfcfcf 70%, #2a2a2a 100%); }

  /* Notebook */
  .notebook { left: 60px; top: 360px; width: 220px; height: 280px; background: var(--notebook); padding: 28px 20px 20px 30px; }
  .notebook .binding { position: absolute; left: 0; top: 0; bottom: 0; width: 16px; height: 280px; }
  .notebook .brand { color: #ffffff; font-size: 15px; justify-content: center; }
  .notebook .brand-dot { width: 8px; height: 8px; }

  /* Letterhead */
  .letterhead { left: 330px; top: 40px; width: 420px; height: 594px; padding: 38px 40px; }
  .letterhead .head { display: flex; justify-content: space-between; align-items: flex-start; }
  .letterhead .brand { font-size: 17px; }
  .letterhead .brand-dot { width: 9px; height: 9px; }
  .letterhead .contact { font-size: 7px; line-height: 1.6; border-left: 2px solid var(--accent); padding-left: 6px; }
  .letterhead .body { margin-top: 60px; width: 250px; font-size: 7px; line-height: 1.6; }
  .letterhead .body p { margin-bottom: 9px; }
  .letterhead .signature { font-family: "Mrs Saint Delafield", cursive; font-size: 30px; margin-top: 4px; line-height: 1; }
  .letterhead .sign-name { font-size: 7px; font-weight: 600; }
  .letterhead .sign-role { font-size: 6.5px; color: var(--ink-soft); }
  .letterhead .foot { position: absolute; right: 40px; bottom: 150px; font-size: 6.5px; color: var(--ink-soft); }

  /* Envelope */
  .envelope { left: 790px; top: 230px; width: 360px; height: 200px; }
  .envelope .return { position: absolute; left: 26px; bottom: 26px; }
  .envelope .brand { font-size: 15px; }
  .envelope .brand-dot { width: 8px; height: 8px; }
  .envelope .contact { margin-top: 6px; font-size: 6.5px; line-height: 1.5; }
</style>
</head>
<body>

  <section class="sheet card-front" aria-label="Business card front">
    <div class="brand"><span class="brand-dot"></span>Velvet Harbor</div>
    <div class="person">Rolf Lindqvist</div>
    <div class="role">Photographer / Owner</div>
    <div class="contact">
      4630 Marlow Ave W Parrish, FL 34218<br>
      rolf@velvetharborphotoworks.com<br>
      www.velvetharborphotoworks.com
    </div>
  </section>

  <section class="sheet card-back" aria-label="Business card back">
    <div class="photo" role="img" aria-label="Black and white photograph of a tattooed subject"></div>
  </section>

  <section class="sheet notebook" aria-label="Notebook cover">
    <svg class="binding" viewBox="0 0 16 280" aria-hidden="true">
      <g fill="none" stroke="var(--binding)" stroke-width="1.5">
        <circle cx="8" cy="14" r="4"/><circle cx="8" cy="30" r="4"/><circle cx="8" cy="46" r="4"/>
        <circle cx="8" cy="62" r="4"/><circle cx="8" cy="78" r="4"/><circle cx="8" cy="94" r="4"/>
        <circle cx="8" cy="110" r="4"/><circle cx="8" cy="126" r="4"/><circle cx="8" cy="142" r="4"/>
        <circle cx="8" cy="158" r="4"/><circle cx="8" cy="174" r="4"/><circle cx="8" cy="190" r="4"/>
        <circle cx="8" cy="206" r="4"/><circle cx="8" cy="222" r="4"/><circle cx="8" cy="238" r="4"/>
        <circle cx="8" cy="254" r="4"/><circle cx="8" cy="270" r="4"/>
      </g>
    </svg>
    <div class="brand"><span class="brand-dot"></span>Velvet Harbor</div>
  </section>

  <section class="sheet letterhead" aria-label="Letterhead">
    <header class="head">
      <div class="brand"><span class="brand-dot"></span>Velvet Harbor</div>
      <div class="contact">
        4630 Marlow Ave W Parrish, FL 34218<br>
        rolf@velvetharborphotoworks.com<br>
        www.velvetharborphotoworks.com
      </div>
    </header>
    <div class="body">
      <p>Dear Client,</p>
      <p>Thank you for choosing our studio to document your work. We look forward to capturing each piece with care and clear, honest light.</p>
      <p>Your session details are attached below. Please review the schedule and let us know if anything should change before the shoot day.</p>
      <p>Warm regards,</p>
      <div class="signature">Rolf Lindqvist</div>
      <div class="sign-name">Rolf Lindqvist</div>
      <div class="sign-role">Photographer / Owner</div>
    </div>
    <div class="foot">Strength, Elegance, and Beauty</div>
  </section>

  <section class="sheet envelope" aria-label="Envelope">
    <div class="return">
      <div class="brand"><span class="brand-dot"></span>Velvet Harbor</div>
      <div class="contact">
        4630 Marlow Ave W Parrish, FL 34218<br>
        www.velvetharborphotoworks.com
      </div>
    </div>
  </section>

</body>
</html>
```